Brightmoor Fire Solutions business card, logo and web design.

We need business cards for our new company. We are based in South Africa. We specialise in fire detection, fire prevention, security, access control and CCTV in buildings. We service and install sprinkler systems, fire hose reals and fire extinguishers in buildings. Our slogan in the company is "Safety on every level" . We strive to be innovators in our field and deliver the best service possible at the best quality. We want to be the best in our field. We don't have any colour preferences as long as it relates to our type of business.
Our target market is clients that owns big buildings with multiple levels, such a malls,office buildings or warehouses.

Target Market(s)

Industry/Entity Type

Fire Safety

Contact Information for Business Card

The front of the card should have the company name (Brightmoor Fire Solutions (PTY) LTD. and a description of the company. Fire engineering & security services.

Logo Text

Safety on every level

Number of Pages Required

4 page

Font styles to use
Serif

Colors

Designer to choose colors to be used in the design.

Requirements
Must have
• The company name, the logo and all the details on the back of the card. It should be simple and not to busy.
Nice to have
• Just something different and new. Brightmoor means - innovate so the card should represent our name.
Should not have
• Small pictures or lots of graphics on.

```html
<!DOCTYPE html>
<html lang="en">
<head>
<meta charset="utf-8">
<title>Brightmoor Fire Solutions – Business Card</title>
<link rel="stylesheet" href="https://fonts.googleapis.com/css2?family=Open+Sans:ital,wght@0,400;0,600;1,600&display=swap">
<style>
  :root {
    --backdrop: #2b2b2b;
    --card-dark: #2a2a2a;
    --card-dark-edge: #1c1c1c;
    --silver-light: #f2f2f2;
    --silver-mid: #cfcfcf;
    --silver-dark: #a9a9a9;
    --flame: #e8572b;
    --ink: #2a2a2a;
    --grey-text: #a3a3a3;
    --grey-dark-text: #5c5c5c;
  }
  * { box-sizing: border-box; margin: 0; padding: 0; }
  html, body {
    width: 1200px; height: 716px; overflow: hidden;
    background: var(--backdrop);
    font-family: "Open Sans", Arial, sans-serif;
  }
  .canvas { position: relative; width: 1200px; height: 716px; }

  .brand-name {
    display: flex; align-items: center;
    font-weight: 600;
    color: var(--flame);
    line-height: 1;
    white-space: nowrap;
  }
  .brand-mark {
    display: inline-block; flex: none;
    background: var(--flame);
    border-radius: 50%;
  }
  .brand-legal, .brand-service {
    font-weight: 400;
    color: var(--grey-text);
    white-space: nowrap;
  }

  /* Front card */
  .card-front {
    position: absolute; left: 60px; top: 60px;
    width: 500px; height: 290px;
    border-radius: 16px;
    background: var(--card-dark);
    box-shadow: 0 0 0 1px var(--card-dark-edge);
    display: flex; flex-direction: column; justify-content: center;
    padding-left: 70px;
  }
  .card-front .brand-name { font-size: 44px; gap: 14px; }
  .card-front .brand-mark { width: 22px; height: 22px; }
  .card-front .brand-legal { font-size: 14px; margin-top: 14px; }
  .card-front .brand-service { font-size: 13px; margin-top: 6px; }
  .card-front .slogan { font-size: 13px; color: var(--grey-text); margin-top: 6px; }

  /* Back card */
  .card-back {
    position: absolute; left: 610px; top: 250px;
    width: 540px; height: 310px;
    border-radius: 16px;
    background: linear-gradient(165deg, var(--silver-mid) 0%, var(--silver-light) 35%, var(--silver-mid) 70%, var(--silver-dark) 100%);
    color: var(--ink);
  }
  .holder { position: absolute; left: 28px; top: 26px; padding-left: 16px; }
  .holder::before {
    content: ""; position: absolute; left: 0; top: 2px;
    width: 7px; height: 36px; background: var(--flame);
  }
  .holder-name { font-size: 20px; font-weight: 600; }
  .holder-role { font-size: 12px; font-style: italic; font-weight: 600; color: var(--flame); }

  .contact-list {
    position: absolute; left: 34px; top: 130px;
    list-style: none; font-size: 14px; font-weight: 600; color: var(--grey-dark-text);
  }
  .contact-list li { display: flex; align-items: center; gap: 8px; height: 24px; }
  .contact-list svg { width: 12px; height: 12px; fill: var(--flame); flex: none; }

  .card-back .logo-block { position: absolute; right: 30px; top: 126px; }
  .card-back .brand-name { font-size: 26px; gap: 8px; }
  .card-back .brand-mark { width: 13px; height: 13px; }
  .card-back .brand-legal { font-size: 10px; margin-top: 6px; color: var(--grey-dark-text); }
  .card-back .brand-service { font-size: 10px; margin-top: 2px; color: var(--grey-dark-text); }

  .website {
    position: absolute; right: 30px; bottom: 22px;
    font-size: 13px; color: var(--flame);
  }

  /* Logo lockup */
  .logo-lockup { position: absolute; left: 46px; top: 566px; }
  .logo-lockup .brand-name { font-size: 52px; gap: 16px; }
  .logo-lockup .brand-mark { width: 26px; height: 26px; }
  .logo-lockup .brand-legal { font-size: 16px; margin-top: 14px; }
  .logo-lockup .brand-service { font-size: 14px; margin-top: 6px; }
</style>
</head>
<body>
<main class="canvas">

  <section class="card-front" aria-label="Business card front">
    <div class="brand-name"><span class="brand-mark"></span>Brightmoor</div>
    <div class="brand-legal">Brightmoor Fire Solutions (PTY) LTD</div>
    <div class="brand-service">Fire engineering &amp; security services</div>
    <div class="slogan">Safety on every level</div>
  </section>

  <section class="card-back" aria-label="Business card back">
    <div class="holder">
      <div class="holder-name">PIETER VAN WYK</div>
      <div class="holder-role">BSc(QS)(UP) . MANAGING DIRECTOR</div>
    </div>

    <ul class="contact-list">
      <li><svg viewBox="0 0 12 12" aria-hidden="true"><path d="M1 4c0-2 2-3 5-3s5 1 5 3l-2 1-1-2H4L3 5zM3 6h6l1 5H2z"/></svg>+27 (0)12 555 0142</li>
      <li><svg viewBox="0 0 12 12" aria-hidden="true"><path d="M3 1h5v3H3zM1 5h10v6H1zM3 7h2v1H3z"/></svg>+27 (0)12 555 0187</li>
      <li><svg viewBox="0 0 12 12" aria-hidden="true"><path d="M3 0h6v12H3zM4 1v8h4V1z"/></svg>+27 (0)83 555 0163</li>
      <li><svg viewBox="0 0 12 12" aria-hidden="true"><path d="M0 2h12v8H0zM1 3l5 4 5-4z"/></svg>pieter@brightmoorfire.co.za</li>
      <li><svg viewBox="0 0 12 12" aria-hidden="true"><path d="M6 0a4 4 0 0 1 4 4c0 3-4 8-4 8S2 7 2 4a4 4 0 0 1 4-4zm0 2.5a1.5 1.5 0 1 0 0 3 1.5 1.5 0 0 0 0-3z"/></svg>14 Kiaat Avenue. Lynnwood Ridge. Pretoria. 0040</li>
    </ul>

    <div class="logo-block">
      <div class="brand-name"><span class="brand-mark"></span>Brightmoor</div>
      <div class="brand-legal">Brightmoor Fire Solutions (PTY) LTD</div>
      <div class="brand-service">Fire engineering &amp; security services</div>
    </div>

    <div class="website">www.brightmoorfire.co.za</div>
  </section>

  <section class="logo-lockup" aria-label="Logo lockup">
    <div class="brand-name"><span class="brand-mark"></span>Brightmoor</div>
    <div class="brand-legal">Brightmoor Fire Solutions (PTY) LTD</div>
    <div class="brand-service">Fire engineering &amp; security services</div>
  </section>

</main>
</body>
</html>
```